Rug Cleaning Web Design Project

We need a web design for our cleaning company. We currently have a web page but are not happy with its design. We currently offer fine rug cleaning,upholstery cleaning, and residential and commercial carpet cleanning. We also offer water damage restoration. For our rug cleaning services we offer : Enzyme treatments for pet contamination and odor removal, application of stain protection that is designed for the fine textiles used in rug construction, application of treatments designed to prevent moth damage and pads designed to be used under rugs.Our current web site is harborfreshcare.example. We are intrested in a design with similar information to the web page of Velmora Rug Cleaners INC. We would like to use the colors that are present in our logo that will be uploaded with this description. We would also like this new page to be linked to our other address loomrinsepro.example. We would like the deign to be visually attractive but not "too busy".
Updates

Please include pictures of rugs, or people washing rugs if possible. We do not offer maid type cleaning services. We would not be interested in designs including pictures depicting that type service. Thanks for your hard work on this project.

Dana Whitlow

Industry/Entity Type

Residential

Requirements
Must have
• This page must be viewable on smart phones and tablets.

```html
<!DOCTYPE html>
<html lang="en">
<head>
<meta charset="utf-8">
<meta name="viewport" content="width=1200">
<title>Loom Rinse Pro</title>
<link rel="stylesheet" href="https://fonts.googleapis.com/css2?family=Source+Sans+3:wght@400;600;700&display=swap">
<style>
  :root {
    --page-bg: #ffffff;
    --brand-blue: #1b7bc1;
    --band-top: #1677bd;
    --band-bottom: #2a8ccd;
    --ink-dark: #1c1c1c;
    --ink-light: #ffffff;
  }
  * { margin: 0; padding: 0; box-sizing: border-box; }
  html, body {
    width: 1200px;
    height: 900px;
    overflow: hidden;
    background: var(--page-bg);
    font-family: "Source Sans 3", "Myriad Pro", Arial, sans-serif;
  }
  .canvas {
    position: relative;
    width: 1200px;
    height: 900px;
  }
  .brand {
    position: absolute;
    left: 380px;
    top: 300px;
    display: flex;
    align-items: center;
    gap: 22px;
    color: var(--ink-dark);
    font-weight: 700;
  }
  .brand-dot {
    width: 74px;
    height: 74px;
    border-radius: 50%;
    background: var(--brand-blue);
    flex: none;
  }
  .brand-text { display: flex; flex-direction: column; line-height: 1; }
  .brand-name { font-size: 56px; letter-spacing: -1px; }
  .brand-sub {
    font-size: 17px;
    letter-spacing: 5px;
    text-transform: uppercase;
    margin-top: 8px;
    align-self: flex-end;
  }
  .nav-band {
    position: absolute;
    left: 0;
    top: 490px;
    width: 1200px;
    height: 197px;
    background: linear-gradient(180deg, var(--band-top), var(--band-bottom) 55%, var(--band-top));
  }
  .nav-rule {
    position: absolute;
    left: 0;
    top: 97px;
    width: 100%;
    height: 2px;
    background: var(--ink-light);
  }
  .nav-link {
    position: absolute;
    top: 50px;
    transform: translateX(-50%);
    color: var(--ink-light);
    font-size: 34px;
    font-weight: 600;
    text-decoration: none;
    white-space: nowrap;
  }
  .nav-link.about { left: 137px; }
  .nav-link.rugs { left: 384px; }
  .nav-link.water { left: 698px; }
  .nav-link.carpet { left: 1011px; }
  .enter-link {
    position: absolute;
    left: 621px;
    top: 148px;
    transform: translateX(-50%);
    color: var(--ink-dark);
    font-size: 32px;
    font-weight: 600;
    text-decoration: underline;
    text-underline-offset: 4px;
    text-shadow: 0 0 2px #fff, 0 0 2px #fff, 1px 1px 1px #fff;
  }
  .site-footer {
    position: absolute;
    left: 0;
    top: 846px;
    width: 1200px;
    height: 54px;
    background: var(--brand-blue);
    color: var(--ink-light);
    font-size: 19px;
    font-weight: 600;
    display: flex;
    align-items: center;
    justify-content: center;
  }
</style>
</head>
<body>
<div class="canvas">
  <header class="brand">
    <span class="brand-dot"></span>
    <span class="brand-text">
      <span class="brand-name">Loom Rinse Pro</span>
      <span class="brand-sub">Harbor Fresh Care, LLC</span>
    </span>
  </header>

  <nav class="nav-band">
    <a class="nav-link about" href="#">About Us</a>
    <a class="nav-link rugs" href="#">Rug Washing</a>
    <a class="nav-link water" href="#">Water Damage</a>
    <a class="nav-link carpet" href="#">Carpet Cleaning</a>
    <span class="nav-rule"></span>
    <a class="enter-link" href="#">Enter Site</a>
  </nav>

  <footer class="site-footer">Copyright &copy; 2012, Loom Rinse Pro</footer>
</div>
</body>
</html>
```